Marlowick APP redesign and color change

I am looking for a new design for my app. Please see the attached current design.

Currently, I have a functioning app but the colors and design are awful!
The logo is great but the rest of the app needs a refresh.
(Logo hi res not yet available but will upload soon.)
New colors or anything that is cutting edge.

Basically: It is a secure social media app within a school system where the teachers, students and parents can text, exchange photos, plan curriculum, etc.

I NEED ONLY landing page with a new look!
Looking for one distinct design for the landing page with new look.
The developer will apply this one design towards the rest of the pages/app screens.

Because part of the social media I need the feel and look of what is now the trend. Something that will attract and keep the client(s) interested. I am really leaving all the creative work to the designer and open to any suggestions.
Updates

Target Market(s)

Schools, community, teachers, students, colleges, sport teams

Industry/Entity Type

Non Profit

Font styles to use
Serif
Sans Serif

Colors

Designer to choose colors to be used in the design.

Requirements
Must have
• Sharp, trendy, millennial feel
Nice to have
• Up to designer
Should not have
• Up to designer

```html
<!DOCTYPE html>
<html lang="en">
<head>
<meta charset="utf-8">
<title>Marlowick — App Screens</title>
<link rel="stylesheet" href="https://fonts.googleapis.com/css2?family=Roboto:wght@400;500&family=Open+Sans:wght@400;600&display=swap">
<style>
:root{
  --orange:#E8961E;
  --orange-deep:#DF8C12;
  --gold-top:#D8A64A;
  --gold-mid:#C8902E;
  --gold-low:#B8842A;
  --olive:#4A4812;
  --ink:#1E1E1E;
  --muted:#7A7A7A;
  --rule:#E4E4E4;
  --bubble:#FCF1E2;
  --white:#FFFFFF;
  --stage:#2A2A2A;
  --avatar:#5E6670;
}
*{box-sizing:border-box;margin:0;padding:0}
html,body{width:1200px;height:960px;overflow:hidden}
body{background:var(--stage);font-family:"Roboto",sans-serif;color:var(--ink);position:relative}
.screens{position:absolute;top:120px;left:0;width:1200px;display:flex;justify-content:space-evenly}
.slot{width:337.5px;height:600.3px;position:relative;overflow:hidden}
.screen{width:375px;height:667px;transform:scale(.9);transform-origin:0 0;position:absolute;top:0;left:0;background:var(--white);overflow:hidden}
.statusbar{height:20px;display:flex;align-items:center;justify-content:space-between;padding:0 6px;font-size:11px;color:var(--white);font-family:"Open Sans",sans-serif}
.statusbar .battery{display:inline-block;width:22px;height:9px;border:1px solid #fff;border-radius:2px;background:#fff;vertical-align:middle;margin-left:3px}
.appbar{background:var(--orange);}
.appbar .titlebar{height:44px;display:flex;align-items:center;justify-content:center;position:relative;color:var(--white);font-size:18px;font-family:"Open Sans",sans-serif}
.appbar .titlebar svg{position:absolute;top:11px}

/* Login */
.login{background:var(--gold-mid)}
.login .backdrop{position:absolute;inset:0;background:linear-gradient(180deg,var(--gold-top) 0%,var(--gold-mid) 45%,var(--gold-low) 80%,#B07E2A 100%)}
.login .statusbar{position:relative}
.brand{position:absolute;top:78px;left:0;width:100%;text-align:center}
.brand .dot{width:70px;height:70px;border-radius:50%;background:var(--olive);opacity:.75;margin:0 auto 36px}
.brand .wordmark{font-size:18px;letter-spacing:9px;color:var(--olive);font-weight:500;padding-left:9px}
.signin-card{position:absolute;left:16px;top:317px;width:346px;height:195px;background:var(--white);border-radius:6px;padding:0 20px}
.field{height:54px;display:flex;align-items:center;border-bottom:1px solid var(--rule);font-size:15px;color:var(--muted)}
.field.password{border-bottom:none;letter-spacing:3px}
.field svg{margin-right:18px;flex:none}
.field .eye{margin-left:auto;margin-right:0}
.card-actions{position:absolute;left:20px;right:16px;bottom:16px;display:flex;align-items:center;justify-content:space-between}
.link-btn{font-size:14px;color:var(--olive);font-weight:500;padding-left:18px}
.pill{background:var(--orange);color:var(--white);font-size:14px;font-weight:500;border-radius:20px;width:110px;height:40px;display:flex;align-items:center;justify-content:center}
.join-bar{position:absolute;left:0;bottom:0;width:100%;height:60px;background:var(--olive);display:flex;align-items:center;justify-content:space-between;padding:0 10px 0 14px;color:var(--white);font-size:16px}
.join-bar .pill{background:var(--white);color:var(--ink);width:104px;font-size:14px}

/* Conversations */
.thread-list{list-style:none}
.thread{height:81px;display:flex;align-items:flex-start;padding:14px 10px 0 15px;position:relative}
.avatar{width:50px;height:50px;border-radius:50%;background:var(--avatar);flex:none;margin-right:14px}
.avatar.warm{background:#8A5A48}
.thread .body{flex:1;padding-top:4px}
.thread .name{font-size:16px;color:var(--ink)}
.thread .preview{font-size:14px;color:var(--muted);margin-top:3px}
.thread.unread .name{font-weight:500}
.thread.unread .preview{color:var(--ink)}
.thread .date{position:absolute;right:10px;top:20px;font-size:14px;color:var(--muted)}
.thread.unread .date{color:var(--ink)}
.fab{position:absolute;left:300px;top:542px;width:60px;height:60px;border-radius:50%;background:var(--orange);display:flex;align-items:center;justify-content:center;box-shadow:0 2px 6px rgba(0,0,0,.25)}
.tabbar{position:absolute;bottom:0;left:0;width:100%;height:50px;background:var(--white);border-top:1px solid var(--rule);display:flex;justify-content:space-around;align-items:center}
.tabbar .active{position:relative}
.tabbar .active::before{content:"";position:absolute;top:-12px;left:2px;width:28px;height:2px;background:var(--orange)}

/* Chat */
.messages{padding:14px 15px 0 15px;display:flex;flex-direction:column}
.msg{display:flex;align-items:flex-start;margin-bottom:20px}
.msg .avatar{margin-right:16px}
.bubble{background:var(--bubble);border-radius:6px;padding:11px 14px;font-size:15px;line-height:20px;color:var(--ink);letter-spacing:-.3px}
.msg.out{justify-content:flex-end}
.msg.out .bubble{background:var(--orange);color:var(--white)}
.stamp{text-align:center;font-size:11px;color:var(--muted);margin:-4px 0 16px}
.composer{position:absolute;bottom:0;left:0;width:100%;height:58px;border-top:1px solid var(--rule);display:flex;align-items:center;justify-content:space-between;padding:0 15px 0 22px;font-size:16px;color:var(--muted)}

.corner-brand{position:absolute;left:40px;bottom:40px;font-size:16px;letter-spacing:8px;color:#E6E6E6;font-weight:500}
</style>
</head>
<body>

<main class="screens">

  <!-- Sign in -->
  <div class="slot">
    <section class="screen login">
      <div class="backdrop" role="img" aria-label="Golden-toned photo of a lone tree in a dry plain under a cloudy sky"></div>
      <div class="statusbar"><span>●●●●● iCorvo</span><span>9:41 AM</span><span>100%<i class="battery"></i></span></div>
      <div class="brand">
        <div class="dot"></div>
        <div class="wordmark">MARLOWICK</div>
      </div>
      <form class="signin-card">
        <div class="field">
          <svg width="20" height="16" viewBox="0 0 20 16" fill="none" stroke="#555" stroke-width="1.3"><rect x="1" y="1" width="18" height="14"/><path d="M1 1l9 7 9-7"/></svg>
          email address
        </div>
        <div class="field password">
          <svg width="18" height="20" viewBox="0 0 18 20" fill="none" stroke="#555" stroke-width="1.3"><rect x="1" y="8" width="16" height="11" rx="1"/><path d="M4 8V5a5 5 0 0110 0v3"/><path d="M9 12v3"/></svg>
          ••••••••
          <svg class="eye" width="22" height="14" viewBox="0 0 22 14" fill="none" stroke="#E8961E" stroke-width="1.4"><path d="M1 7c3-5 7-6 10-6s7 1 10 6c-3 5-7 6-10 6S4 12 1 7z"/><circle cx="11" cy="7" r="3"/></svg>
        </div>
        <div class="card-actions">
          <span class="link-btn">FORGOT PASSWORD</span>
          <span class="pill">SIGN IN</span>
        </div>
      </form>
      <div class="join-bar"><span>Not a member?</span><span class="pill">JOIN NOW</span></div>
    </section>
  </div>

  <!-- Conversations -->
  <div class="slot">
    <section class="screen">
      <header class="appbar">
        <div class="statusbar"><span>●●●●● Corvo</span><span>7:28 AM</span><span>100%<i class="battery"></i></span></div>
        <div class="titlebar">Conversations
          <svg style="right:14px" width="22" height="22" viewBox="0 0 22 22" fill="none" stroke="#fff" stroke-width="1.6"><circle cx="9" cy="9" r="7"/><path d="M14 14l6 6"/></svg>
        </div>
      </header>
      <ul class="thread-list">
        <li class="thread unread"><span class="avatar" role="img" aria-label="Contact photo"></span><div class="body"><div class="name">Nolan Pryce</div><div class="preview">Hey there!</div></div><span class="date">18 Jul</span></li>
        <li class="thread"><span class="avatar warm" role="img" aria-label="Contact photo"></span><div class="body"><div class="name">Adaeze Marie Okafor</div><div class="preview">Okay. Just received it. Thanks!</div></div><span class="date">13 Jul</span></li>
        <li class="thread"><span class="avatar" role="img" aria-label="Contact photo"></span><div class="body"><div class="name">Derek Holloway</div><div class="preview">Yeah. It works.</div></div><span class="date">4 Jul</span></li>
        <li class="thread unread"><span class="avatar" role="img" aria-label="Contact photo"></span><div class="body"><div class="name">Julian Marsh</div><div class="preview">Would you mind to send it again?</div></div><span class="date">26 Jun</span></li>
        <li class="thread"><span class="avatar" role="img" aria-label="Contact photo"></span><div class="body"><div class="name">Nolan Pryce</div><div class="preview">Hey there!</div></div><span class="date">9 Jun</span></li>
        <li class="thread"><span class="avatar warm" role="img" aria-label="Contact photo"></span><div class="body"><div class="name">Adaeze Marie Okafor</div><div class="preview">Okay. Just received it. Thanks!</div></div><span class="date">30 May</span></li>
        <li class="thread"><span class="avatar" role="img" aria-label="Contact photo"></span><div class="body"><div class="name">Derek Holloway</div><div class="preview">Yeah. It works.</div></div><span class="date">1 May</span></li>
      </ul>
      <div class="fab">
        <svg width="26" height="26" viewBox="0 0 26 26" fill="none" stroke="#fff" stroke-width="1.6"><path d="M12 3H3v20h20v-9"/><path d="M20 2l4 4-11 11H9v-4z"/></svg>
      </div>
      <nav class="tabbar">
        <svg class="active" width="30" height="26" viewBox="0 0 30 26" fill="none" stroke="#E8961E" stroke-width="1.6"><path d="M3 3h20v14H12l-6 5v-5H3z"/><circle cx="10" cy="10" r="1.5"/><circle cx="16" cy="10" r="1.5"/></svg>
        <svg width="26" height="26" viewBox="0 0 26 26" fill="none" stroke="#999" stroke-width="1.6"><rect x="2" y="2" width="9" height="9"/><rect x="15" y="2" width="9" height="9"/><rect x="2" y="15" width="9" height="9"/><rect x="15" y="15" width="9" height="9"/></svg>
        <svg width="28" height="26" viewBox="0 0 28 26" fill="none" stroke="#999" stroke-width="1.6"><circle cx="13" cy="8" r="6"/><path d="M2 25c1-7 6-10 11-10s10 3 11 10z"/></svg>
        <svg width="26" height="26" viewBox="0 0 26 26" fill="none" stroke="#999" stroke-width="1.6"><path d="M3 23l11-11"/><path d="M14 12a6 6 0 008-8l-3 3-3-1-1-3 3-3a6 6 0 00-8 8"/><path d="M4 3l4 4M16 16l7 7"/></svg>
      </nav>
    </section>
  </div>

  <!-- Chat -->
  <div class="slot">
    <section class="screen">
      <header class="appbar">
        <div class="statusbar"><span>●●●●● Corvo</span><span>7:28 AM</span><span>100%<i class="battery"></i></span></div>
        <div class="titlebar">Julian Marsh
          <svg style="left:14px" width="22" height="20" viewBox="0 0 22 20" fill="none" stroke="#fff" stroke-width="1.6"><path d="M8 3L2 9l6 6"/><path d="M2 9h11a7 7 0 017 7v2"/></svg>
        </div>
      </header>
      <div class="messages">
        <div class="msg"><span class="avatar" role="img" aria-label="Contact photo"></span><div class="bubble" style="width:240px">So, do you have any plan this afternoon?</div></div>
        <div class="msg out"><div class="bubble">Group Study. You up?</div></div>
        <div class="msg"><span class="avatar" role="img" aria-label="Contact photo"></span><div class="bubble">Sure thing. See yah later!</div></div>
        <div class="msg out"><div class="bubble">Okeydokey :)</div></div>
        <div class="stamp">Today, 14:28</div>
        <div class="msg out"><div class="bubble" style="width:229px">Hey! We're here at the library. Where are you?</div></div>
      </div>
      <div class="composer"><span>Type a message</span>
        <svg width="36" height="36" viewBox="0 0 36 36" fill="none" stroke="#E8961E" stroke-width="1.6"><circle cx="18" cy="18" r="16"/><path d="M10 17l15-6-6 15-2-6z"/></svg>
      </div>
    </section>
  </div>

</main>

<div class="corner-brand">MARLOWICK</div>

</body>
</html>
```